Upscale business cards needed for Board of Directors

We need professional business cards created for members of our family business Board of Directors. We would like these relatively simple and straightforward, but also with a unique element to set them apart. Probably stick with neutral and simple colors - white, grey etc. We need space for the traditional elements, including name, title, address, email/phone number. And we will be creating several from this template so it needs to be template that is easy to switch information in and out of.
Business
See description

```html
<!DOCTYPE html>
<html lang="en">
<head>
<meta charset="utf-8">
<title>Harborline Holdings – Business Card</title>
<link href="https://fonts.googleapis.com/css2?family=Roboto:wght@400;500;700&display=swap" rel="stylesheet">
<style>
  :root{
    --backdrop:#2e2e30;
    --card-white:#ffffff;
    --card-black:#17151a;
    --ink:#1d1d1f;
    --ink-soft:#4a4a4d;
    --rule:#b9b9bc;
    --gold:#b39f77;
    --band-dark:#2a282c;
  }
  *{box-sizing:border-box;margin:0;padding:0}
  html,body{width:1200px;height:843px;overflow:hidden}
  body{background:var(--backdrop);font-family:"Roboto",Arial,sans-serif;position:relative}
  .card{position:absolute;top:267px;width:540px;height:308px;overflow:hidden;border-radius:2px;box-shadow:0 10px 30px rgba(0,0,0,.45)}
  .card--back{left:40px;background:var(--card-black)}
  .card--front{left:620px;background:var(--card-white)}

  .wordmark{font-weight:700;text-transform:uppercase;line-height:1}
  .card--back .wordmark{position:absolute;left:0;right:0;top:112px;text-align:center;color:#fff}
  .wordmark__main{display:block;font-size:36px;letter-spacing:1px}
  .wordmark__sub{display:block;font-size:17px;letter-spacing:9px;margin-top:6px}
  .back-web{position:absolute;left:0;right:0;bottom:34px;text-align:center;color:#9c9ca0;font-size:12px;letter-spacing:1px}

  .card--front .wordmark{position:absolute;right:36px;top:50px;text-align:center;color:var(--ink)}
  .card--front .wordmark__main{font-size:30px}
  .card--front .wordmark__sub{font-size:14px;letter-spacing:8px;margin-top:5px}

  .person{position:absolute;left:36px;top:92px}
  .person__name{font-size:17px;font-weight:500;color:var(--ink)}
  .person__title{font-size:13px;color:var(--gold);margin-top:3px}

  .rule{position:absolute;height:1px;background:var(--rule)}
  .rule--main{left:36px;right:36px;top:140px}
  .rule--address{left:300px;right:36px;top:214px}

  .contacts{position:absolute;left:36px;top:154px;list-style:none}
  .contacts li{display:flex;align-items:center;gap:10px;font-size:12px;color:var(--ink-soft);height:21px}
  .contacts svg{width:11px;height:11px;fill:var(--ink)}

  .address{position:absolute;right:36px;top:226px;text-align:right;font-size:13px;line-height:18px;color:var(--ink-soft)}

  .footer-band{position:absolute;left:0;bottom:0;width:540px;height:18px}
</style>
</head>
<body>

<section class="card card--back" aria-label="Card back">
  <div class="wordmark">
    <span class="wordmark__main">Harborline</span>
    <span class="wordmark__sub">Holdings</span>
  </div>
  <p class="back-web">www.harborline.com</p>
</section>

<section class="card card--front" aria-label="Card front">
  <div class="wordmark">
    <span class="wordmark__main">Harborline</span>
    <span class="wordmark__sub">Holdings</span>
  </div>

  <div class="person">
    <p class="person__name">Martin Hale</p>
    <p class="person__title">President</p>
  </div>

  <div class="rule rule--main"></div>

  <ul class="contacts">
    <li><svg viewBox="0 0 12 12"><path d="M2.5 1h2l1 2.5-1.3 1a6.5 6.5 0 0 0 3.3 3.3l1-1.3L11 7.5v2a1.5 1.5 0 0 1-1.5 1.5A8.5 8.5 0 0 1 1 2.5 1.5 1.5 0 0 1 2.5 1z"/></svg>555 0142 7788</li>
    <li><svg viewBox="0 0 12 12"><path d="M1 2.5h10v7H1z M1.5 3l4.5 3.5L10.5 3" fill="none" stroke="#1d1d1f" stroke-width="1.2"/></svg>martin@harborline.com</li>
    <li><svg viewBox="0 0 12 12"><circle cx="6" cy="6" r="5"/></svg>www.harborline.com</li>
  </ul>

  <div class="rule rule--address"></div>
  <p class="address">2710 Calloway Street<br>Brook Haven, NY 11720</p>

  <svg class="footer-band" viewBox="0 0 540 18" preserveAspectRatio="none" aria-hidden="true">
    <polygon points="0,0 252,0 240,18 0,18" fill="var(--band-dark)"/>
    <polygon points="256,0 540,0 540,18 244,18" fill="var(--gold)"/>
  </svg>
</section>

</body>
</html>
```